Design cover for information booklet
I am looking for a design for the front and back cover of an information booklet. Also an inside page basic design.
The booklet will contain 10 double sided pages providing information on weight loss surgery.
See my website www.brevinmarsh.com.au for what I do and typical colour themes.
I would also like some theming/illustration which can be utilised on each inside page of the booklet, rather than the pages just being blank with text etc. What would a blank page on this inside of the booklet look like under the design theme that you have created?
My company is Kestrel Institute for Metabolic Surgery. You will find uploaded a Logo for Kestrel Institute for Metabolic Surgery as well as my other logo which is my name “Brevin Marsh, etc.”. The Kestrel Institute for Metabolic Surgery logo should be utilised. The other logo (Brevin Marsh) is optional.
The front cover should contain the following text as minimum:
Kestrel Institute for Metabolic Surgery
Mr Brevin Marsh MBBS FRACS GradCert (Health Stats)
Our tagline is “Experience, Expertise and Empathy”. This should probably be on the front cover also.
The back cover contains (as a minimum) our address, phone number, fax number:
Suite 17, Level 3
Tallowgate Northern Hospital
9 Pemberly Road, Fernwick VIC 3174
Phone: 03 9412 6083
Fax: 03 9417 2865
Email: info@kestrelims.com.au
The files should be in a form whereby the text can be edited and changed if need be.
1. problems with initial graphical attachments - Artforge end 2. several requests by designers for extension

```html
<!DOCTYPE html>
<html lang="en">
<head>
<meta charset="utf-8">
<title>Kestrel Institute for Metabolic Surgery – Booklet Cover</title>
<link rel="stylesheet" href="https://fonts.googleapis.com/css2?family=Montserrat:ital,wght@0,600;0,700;0,800;1,500&display=swap">
<style>
  :root {
    --teal-top: #45b0cb;
    --teal-mid: #5fc0cd;
    --teal-bottom: #92d6c6;
    --white: #ffffff;
    --band-grey: #d9dcdc;
    --deep-teal: #1f6f6a;
    --ribbon-dark: #1d5e5a;
    --ribbon-silver: #c9d0d0;
    --slate: #55606a;
  }
  * { margin: 0; padding: 0; box-sizing: border-box; }
  html, body { width: 847px; height: 1200px; overflow: hidden; background: var(--white); }
  .cover {
    position: relative;
    width: 847px;
    height: 1200px;
    overflow: hidden;
    font-family: "Montserrat", Arial, sans-serif;
    background: linear-gradient(180deg, var(--teal-top) 0%, var(--teal-mid) 45%, var(--teal-bottom) 90%);
  }
  .title-main {
    position: absolute;
    left: 43px;
    top: 99px;
    width: 763px;
    text-align: center;
    font-weight: 800;
    font-size: 150px;
    line-height: 1;
    letter-spacing: 2px;
    color: var(--white);
  }
  .title-second {
    position: absolute;
    left: 108px;
    top: 252px;
    font-weight: 800;
    font-size: 56px;
    line-height: 1;
    color: var(--white);
    white-space: nowrap;
  }
  .title-tail {
    position: absolute;
    right: 37px;
    top: 262px;
    text-align: right;
    color: var(--white);
    font-weight: 800;
    line-height: 1;
    white-space: nowrap;
  }
  .title-tail .line1 { display: block; }
  .title-tail .for { font-size: 36px; }
  .title-tail .big { font-size: 44px; }
  .title-tail .line2 { display: block; font-size: 44px; margin-top: 8px; }
  .tagline {
    position: absolute;
    left: 121px;
    top: 308px;
    font-style: italic;
    font-weight: 500;
    font-size: 15px;
    color: var(--white);
    white-space: nowrap;
  }
  .surgeon {
    position: absolute;
    left: 146px;
    top: 342px;
    font-weight: 700;
    font-size: 11px;
    line-height: 1.5;
    letter-spacing: 0.4px;
    text-transform: uppercase;
    color: var(--white);
    white-space: nowrap;
  }
  .ribbon-art {
    position: absolute;
    left: 180px;
    top: 400px;
    width: 440px;
    height: 620px;
    border-radius: 220px;
    background: linear-gradient(160deg, var(--ribbon-silver) 0%, var(--ribbon-dark) 40%, var(--ribbon-silver) 70%, var(--ribbon-dark) 100%);
    opacity: 0.55;
  }
  .footer-band {
    position: absolute;
    left: 0;
    bottom: 0;
    width: 847px;
    height: 130px;
    background: var(--white);
    border-top: 8px solid var(--band-grey);
  }
  .surgeon-mark {
    position: absolute;
    left: 88px;
    top: 30px;
    font-weight: 700;
    font-size: 34px;
    color: var(--deep-teal);
    display: flex;
    align-items: center;
    gap: 14px;
  }
  .surgeon-mark .dot {
    width: 44px; height: 44px; border-radius: 50%;
    background: var(--deep-teal);
  }
  .surgeon-mark small {
    display: block;
    font-size: 12px;
    letter-spacing: 1px;
    text-transform: uppercase;
  }
  .centre-mark {
    position: absolute;
    left: 624px;
    top: 18px;
    display: flex;
    align-items: center;
    gap: 10px;
    font-weight: 700;
    font-size: 14px;
    color: var(--slate);
  }
  .centre-mark .square {
    width: 60px; height: 80px;
    background: var(--slate);
  }
</style>
</head>
<body>
<main class="cover">
  <h1>
    <span class="title-main">KESTREL</span>
    <span class="title-second">INSTITUTE</span>
    <span class="title-tail"><span class="line1"><span class="for">FOR</span> <span class="big">METABOLIC</span></span><span class="line2">SURGERY</span></span>
  </h1>
  <p class="tagline">“Experience, Expertise and Empathy”</p>
  <p class="surgeon">Mr Brevin Marsh<br>MBBS FRACS GradCert - Health Stats</p>

  <div class="ribbon-art" role="img" aria-label="Illustration of a teal and silver measuring tape twisting down the page in an S shape"></div>

  <footer class="footer-band">
    <div class="surgeon-mark">
      <span class="dot"></span>
      <span>Brevin Marsh<small>General, Upper GI &amp; Bariatric Surgeon</small></span>
    </div>
    <div class="centre-mark">
      <span class="square"></span>
      <span>Kestrel<br>Institute</span>
    </div>
  </footer>
</main>
</body>
</html>
```